Business card and stationery for new company
Member of Verola Group
Business card and stationery for new company - Aviation
Creative Brief
Professional
Bayu Santoso Wiratmaja
Managing Director
Jalan Cemara Lestari III no 8 Sukamulya Tengah South Jakarta 12450
+62 21 57186324 (Ext 204)
bayu.wiratmaja@verola-group.example

```html
<!DOCTYPE html>
<html lang="en">
<head>
<meta charset="utf-8">
<title>Nusa Aero Perkasa — Business Card</title>
<link rel="stylesheet" href="https://fonts.googleapis.com/css2?family=Arimo:wght@400;500&display=swap">
<style>
  :root {
    --backdrop: #2b2b2e;
    --card: #f7f7f8;
    --brand: #3d3a8f;
    --ink: #4a4a52;
    --muted: #7a7a84;
    --rule: #c4c3dc;
  }
  * { box-sizing: border-box; margin: 0; padding: 0; }
  html, body { width: 1200px; height: 881px; overflow: hidden; }
  body {
    background: var(--backdrop);
    font-family: "Arimo", Arial, sans-serif;
    position: relative;
  }
  .card {
    position: absolute;
    width: 520px;
    height: 336px;
    background: var(--card);
    box-shadow: 0 14px 34px rgba(0,0,0,.45);
    overflow: hidden;
  }
  .card--front { left: 50px; top: 272px; }
  .card--back  { left: 630px; top: 272px; }

  .card__band {
    position: absolute; left: 0; right: 0; bottom: 0;
    height: 8px; background: var(--brand);
  }

  .brand-name {
    position: absolute;
    display: flex; align-items: center;
    font-family: "Arimo", Arial, sans-serif;
    font-weight: 400;
    color: var(--brand);
    white-space: nowrap;
  }
  .brand-name__mark { flex: none; background: var(--brand); }

  .card--front .brand-name { left: 34px; top: 150px; font-size: 15px; gap: 8px; }
  .card--front .brand-name__mark { width: 10px; height: 10px; }

  .card--back .brand-name { left: 200px; top: 232px; font-size: 22px; gap: 12px; }
  .card--back .brand-name__mark { width: 14px; height: 14px; }

  .contact {
    position: absolute; left: 242px; top: 40px; width: 256px;
    padding-left: 16px;
    border-left: 1px solid var(--rule);
    color: var(--ink);
  }
  .contact__name { font-size: 15px; font-weight: 500; color: var(--brand); }
  .contact__role { font-size: 10.5px; color: var(--muted); margin-top: 3px; }
  .contact__address { font-size: 10.5px; line-height: 1.45; margin-top: 18px; width: 210px; }
  .contact__lines { list-style: none; margin-top: 16px; }
  .contact__lines li {
    display: flex; align-items: center; gap: 8px;
    font-size: 10.5px; line-height: 1.75;
    white-space: nowrap;
  }
  .contact__lines svg { width: 10px; height: 10px; flex: none; fill: var(--ink); }
</style>
</head>
<body>

  <section class="card card--front" aria-label="Business card front">
    <div class="brand-name"><span class="brand-name__mark"></span>Nusa Aero Perkasa</div>

    <div class="contact">
      <p class="contact__name">Bayu Santoso Wiratmaja</p>
      <p class="contact__role">Managing Director</p>
      <p class="contact__address">Jalan Cemara Lestari III no 8 Sukamulya Tengah South Jakarta 12450</p>
      <ul class="contact__lines">
        <li>
          <svg viewBox="0 0 10 10"><path d="M2 0.5h2l0.8 2.3-1.2 0.9a5.5 5.5 0 0 0 2.7 2.7l0.9-1.2 2.3 0.8v2a1 1 0 0 1-1 1A8 8 0 0 1 1 1.5a1 1 0 0 1 1-1z"/></svg>
          +62 21 57186324 (Ext 204)
        </li>
        <li>
          <svg viewBox="0 0 10 10"><rect x="2.5" y="0.5" width="5" height="9" rx="1"/><rect x="3.4" y="1.6" width="3.2" height="5.6" fill="#f7f7f8"/></svg>
          +62 812 4417 2093
        </li>
        <li>
          <svg viewBox="0 0 10 10"><rect x="0.5" y="3.5" width="9" height="5" rx="0.8"/><rect x="2.5" y="0.8" width="5" height="3"/><rect x="2.5" y="6" width="5" height="1.2" fill="#f7f7f8"/></svg>
          +62 21 57186325
        </li>
        <li>
          <svg viewBox="0 0 10 10"><rect x="0.5" y="2" width="9" height="6.2" rx="0.6"/><path d="M0.9 2.4 5 5.6l4.1-3.2" fill="none" stroke="#f7f7f8" stroke-width="0.9"/></svg>
          bayu.wiratmaja@verola-group.example
        </li>
      </ul>
    </div>

    <div class="card__band"></div>
  </section>

  <section class="card card--back" aria-label="Business card back">
    <div class="brand-name"><span class="brand-name__mark"></span>Nusa Aero Perkasa</div>
  </section>

</body>
</html>
```